Lorvena Aesthetic Doctor

I require an elegant, luxurious looking business card for my aesthetic business. I am a doctor and that will set me aside from competitors. I am planning to provide home and spa based treatments to clients with high expectations. I have attached my logo.

```html
<!DOCTYPE html>
<html lang="en">
<head>
<meta charset="utf-8">
<title>Lorvena Aesthetic Doctor – Business Card</title>
<link href="https://fonts.googleapis.com/css2?family=Quicksand:wght@400;500;600&display=swap" rel="stylesheet">
<style>
  :root {
    --backdrop: #3ebfea;
    --card: #ffffff;
    --ink: #2f3336;
    --grey: #8d9194;
    --accent: #29abe2;
  }
  * { box-sizing: border-box; margin: 0; padding: 0; }
  html, body {
    width: 1200px; height: 800px; overflow: hidden;
    background: var(--backdrop);
    font-family: "Quicksand", sans-serif;
    color: var(--ink);
  }
  .sheet {
    width: 1200px; height: 800px;
    display: flex; align-items: center; justify-content: center; gap: 80px;
  }
  .card {
    width: 360px; height: 580px;
    background: var(--card);
    border-radius: 44px;
    display: flex; flex-direction: column; align-items: center; justify-content: center;
    text-align: center;
    box-shadow: 0 18px 40px rgba(0, 60, 90, 0.18);
  }
  /* Front */
  .brand { display: flex; align-items: center; gap: 14px; }
  .brand-dot {
    width: 46px; height: 46px; border-radius: 50%;
    background: var(--accent);
  }
  .brand-name {
    font-size: 34px; font-weight: 500; letter-spacing: 3px;
    color: var(--grey); text-transform: uppercase;
  }
  .brand-title {
    margin-top: 10px;
    font-size: 17px; font-weight: 500; letter-spacing: 3px;
    color: var(--grey); text-transform: uppercase;
  }
  .brand-tagline {
    margin-top: 14px; font-size: 15px; color: var(--ink); letter-spacing: 0.5px;
  }
  /* Back */
  .doctor-name { font-size: 21px; font-weight: 500; letter-spacing: 0.5px; }
  .doctor-name .post-nominals { font-size: 11px; letter-spacing: 0.5px; }
  .qualification { margin-top: 6px; font-size: 13.5px; color: var(--accent); letter-spacing: 0.4px; }
  .contact-list { list-style: none; margin-top: 28px; display: flex; flex-direction: column; gap: 12px; }
  .contact-item { display: flex; align-items: center; gap: 12px; font-size: 16px; letter-spacing: 0.6px; }
  .contact-item svg { width: 22px; height: 22px; flex: none; }
  .contact-item .highlight { color: var(--accent); }
  .social { margin-top: 18px; display: flex; gap: 12px; }
  .social-dot { width: 20px; height: 20px; border-radius: 50%; background: var(--accent); }
  .social-square { width: 20px; height: 20px; border-radius: 5px; border: 2px solid var(--accent); }
  .services { list-style: none; margin-top: 24px; font-size: 14px; line-height: 1.55; letter-spacing: 0.3px; }
  .rule { margin-top: 14px; width: 14px; height: 2px; background: var(--accent); }
</style>
</head>
<body>
<main class="sheet">
  <section class="card card-front">
    <div class="brand">
      <span class="brand-name">Lorvena</span>
      <span class="brand-dot"></span>
    </div>
    <p class="brand-title">Aesthetic Doctor</p>
    <p class="brand-tagline">Home and Spa Based Treatments</p>
  </section>

  <section class="card card-back">
    <h1 class="doctor-name">Dr. Mirela Voss <span class="post-nominals">MRCPCH MD</span></h1>
    <p class="qualification">Australasian Diploma of Aesthetic Medicine</p>
    <ul class="contact-list">
      <li class="contact-item">
        <svg viewBox="0 0 22 22" aria-hidden="true"><circle cx="11" cy="11" r="11" fill="#29abe2"/><path d="M8 6.5l2 2-1.2 1.4a6 6 0 0 0 3.3 3.3l1.4-1.2 2 2-1.3 1.5C10.8 15.3 6.7 11.2 6.5 7.8z" fill="#fff"/></svg>
        <span>0800 555 019</span>
      </li>
      <li class="contact-item">
        <svg viewBox="0 0 22 22" aria-hidden="true"><circle cx="11" cy="11" r="11" fill="#29abe2"/><rect x="6" y="7.5" width="10" height="7" rx="1" fill="#fff"/><path d="M6.5 8l4.5 3.5L15.5 8" fill="none" stroke="#29abe2" stroke-width="1"/></svg>
        <span>mirela@lorvena.co.nz</span>
      </li>
      <li class="contact-item">
        <svg viewBox="0 0 22 22" aria-hidden="true"><circle cx="11" cy="11" r="11" fill="#29abe2"/><rect x="5.5" y="9" width="6" height="4" rx="2" fill="none" stroke="#fff" stroke-width="1.4"/><rect x="10.5" y="9" width="6" height="4" rx="2" fill="none" stroke="#fff" stroke-width="1.4"/></svg>
        <span>www.<span class="highlight">lorvena</span>.co.nz</span>
      </li>
    </ul>
    <div class="social">
      <span class="social-dot"></span>
      <span class="social-square"></span>
    </div>
    <ul class="services">
      <li>Dermal injectables | Plasma facials</li>
      <li>Microneedling | Skin boosters</li>
      <li>Excessive sweating</li>
      <li>Home and Spa Based Treatments</li>
    </ul>
    <span class="rule"></span>
  </section>
</main>
</body>
</html>
```